Corvell Ashdown Website

Updated website for Corvell Ashdown Dry Cleaners & Garment Care.

Please look at www.tindalepressers.example we really like this site!!!

We are not set on colors or fonts. Looking for an professional easy to use site that looks and works even better on a mobile device. 90% of our customers visit us on cell phones.

Target Market(s)

We are located in an up scale area with young trendy individuals but, also very successful mature customers as well. Probably geared more to tech savvy younger crowd.

Industry/Entity Type

Dry Cleaning

Coding

Coded - Design and coding required

Font styles to use
Serif
Script

Colors
85abd2
85cae6
cee9f5
cfdeed
757575

Requirements
Must have
• Must look good on a mobile device and have sign up for our pick up and delivery. Geographical pick up and delivery perimeters would be great as well. Capturing emails and other user data for future marketing. We do a lot of advertising.
• Please look at www.tindalepressers.example we really like this site!!!
• Search engine optimized.
• Also we are adding a new POS system that will have a login for customers and possibly an app.
Nice to have
• 100% satisfaction guaranteed and scrolling reviews somewhere on the page.

```html
<!DOCTYPE html>
<html lang="en">
<head>
<meta charset="utf-8">
<title>Corvell Ashdown – Satisfaction Guarantee</title>
<link rel="stylesheet" href="https://fonts.googleapis.com/css2?family=Source+Sans+3:wght@400;700;900&display=swap">
<style>
  :root {
    --navy: #152a78;
    --white: #ffffff;
    --hero-dark: #47557a;
    --hero-mid: #5e6c8f;
    --hero-light: #7a86a3;
    --basket: #8a7f86;
    --rule: #2b3350;
  }
  * { box-sizing: border-box; margin: 0; padding: 0; }
  html, body { width: 1200px; height: 759px; overflow: hidden; background: var(--white); }
  body { font-family: "Source Sans 3", "Source Sans Pro", sans-serif; position: relative; }

  .site-header {
    position: absolute; left: 0; top: 0; width: 1200px; height: 158px;
    background: var(--white); z-index: 3;
  }
  .brand-block {
    position: absolute; left: 30px; top: 0; width: 263px; height: 221px;
    background: var(--navy); z-index: 4;
    display: flex; flex-direction: column; align-items: center; justify-content: center; gap: 18px;
  }
  .brand-dot { width: 70px; height: 70px; border-radius: 50%; background: var(--white); }
  .brand-name {
    color: var(--white); font-weight: 700; font-size: 22px; letter-spacing: 0.5px;
  }
  .header-cta {
    position: absolute; left: 791px; top: 40px; width: 287px; height: 74px;
    background: var(--navy); color: var(--white);
    display: flex; align-items: center; justify-content: center;
    font-weight: 700; font-size: 21px; letter-spacing: 2.5px; text-decoration: none;
  }
  .menu-toggle { position: absolute; left: 1105px; top: 61px; width: 41px; height: 32px; }

  .hero {
    position: absolute; left: 0; top: 158px; width: 1200px; height: 601px; overflow: hidden;
  }
  .hero-photo {
    position: absolute; inset: 0;
    background:
      radial-gradient(ellipse 60% 45% at 50% 62%, var(--basket) 0%, transparent 70%),
      linear-gradient(180deg, var(--hero-light) 0%, var(--hero-mid) 45%, var(--hero-dark) 100%);
  }
  .guarantee-seal {
    position: absolute; left: 529px; top: -90px; width: 150px; height: 150px;
    border: 4px solid rgba(255,255,255,0.85); border-radius: 50%;
  }
  .hero-title {
    position: absolute; left: 0; top: 296px; width: 100%; transform: translateY(-50%);
    margin-top: -110px;
    text-align: center; color: var(--white); font-weight: 900; font-size: 76px; letter-spacing: -0.5px;
  }
  .hero-text {
    position: absolute; left: 0; top: 285px; width: 100%; text-align: center;
    color: var(--white); font-size: 24px;
  }
  .hero-cta {
    position: absolute; left: 380px; top: 420px; width: 439px; height: 92px;
    background: var(--navy); color: var(--white);
    display: flex; align-items: center; justify-content: center;
    font-weight: 700; font-size: 21px; letter-spacing: 7px; text-decoration: none;
  }
</style>
</head>
<body>
  <header class="site-header">
    <a class="brand-block" href="#">
      <span class="brand-dot"></span>
      <span class="brand-name">CORVELL ASHDOWN</span>
    </a>
    <a class="header-cta" href="#">SCHEDULE PICKUP</a>
    <svg class="menu-toggle" viewBox="0 0 41 32" aria-label="Menu">
      <rect x="0" y="2" width="41" height="4" fill="var(--rule)"/>
      <rect x="0" y="14" width="41" height="4" fill="var(--rule)"/>
      <rect x="0" y="26" width="41" height="4" fill="var(--rule)"/>
    </svg>
  </header>

  <section class="hero">
    <div class="hero-photo" role="img" aria-label="Wicker laundry basket filled with fresh white towels"></div>
    <div class="guarantee-seal"></div>
    <h1 class="hero-title">Satisfaction Guarantee</h1>
    <p class="hero-text">If we do not meet the results we promised, we will redo the item for free</p>
    <a class="hero-cta" href="#">SCHEDULE PICKUP</a>
  </section>
</body>
</html>
```